Professional Business Card for a Chief Operating Officer

An exciting business card that's professional for a c-suite position.
Parent company on the front with information. (MAPLE ROCK)
3 Brands on the back in a dark blue background.

No icons for phone, email or address.
The card can be vertically laid out or horizontally, whichever fits best.

I'd like to see designs in both formats.
Cards can be designed with a "linen" look or embossed with tone-on-tone as an option.

Target Market(s)

Industry professionals, customers and vendors

Industry/Entity Type

Car Wash

Contact Information for Business Card

Name, title, address, phone, email and logo

Colors
0054AA
0677BA
7BADD7
CADEEF
E8F1F8

Requirements
Must have
• A professional conservative look
Nice to have
• Parent Brand on front, Brand logos on back
Should not have
• Icons

```html
<!DOCTYPE html>
<html lang="en">
<head>
<meta charset="utf-8">
<title>Maple Rock – Business Card</title>
<link rel="stylesheet" href="https://fonts.googleapis.com/css2?family=Arimo:wght@400;700&display=swap">
<style>
  :root {
    --backdrop: #e4e4e2;
    --card-navy: #15204a;
    --card-navy-deep: #101a3c;
    --card-edge: #2f6cae;
    --brand-blue: #4a8fd0;
    --accent-light: #7badd7;
    --rule: #cadeef;
    --text-white: #e8f1f8;
  }
  * { margin: 0; padding: 0; box-sizing: border-box; }
  html, body { width: 1200px; height: 801px; overflow: hidden; }
  body {
    background: var(--backdrop);
    font-family: "Arimo", Arial, sans-serif;
    position: relative;
  }
  .card {
    position: absolute;
    top: 240px;
    width: 540px;
    height: 309px;
    border-radius: 3px;
    box-shadow: 0 0 0 2px var(--card-edge), 0 14px 30px rgba(0,0,0,.25);
    overflow: hidden;
  }
  .card--front { left: 40px; background: var(--card-navy); }
  .card--back {
    left: 620px;
    background: radial-gradient(ellipse at 50% 40%, #1f2f66 0%, var(--card-navy) 55%, var(--card-navy-deep) 100%);
  }

  /* Front */
  .parent-mark {
    position: absolute;
    left: 210px; top: 44px;
    display: flex; align-items: center; gap: 14px;
    white-space: nowrap;
  }
  .parent-mark__dot {
    width: 64px; height: 64px; border-radius: 50%;
    background: var(--brand-blue);
    flex: none;
  }
  .parent-mark__name {
    font-weight: 700; font-size: 32px; letter-spacing: 1px;
    color: var(--brand-blue);
  }
  .person {
    position: absolute; left: 36px; top: 138px;
  }
  .person__name {
    font-weight: 700; font-size: 22px; letter-spacing: .5px;
    color: var(--brand-blue); text-transform: uppercase;
    white-space: nowrap;
  }
  .person__title {
    font-size: 15px; color: var(--text-white); margin-top: 4px;
    white-space: nowrap;
  }
  .divider {
    position: absolute; left: 36px; right: 36px; top: 196px;
    height: 1px; background: var(--rule); opacity: .85;
  }
  .contact-list {
    position: absolute; left: 36px; top: 212px;
    list-style: none;
  }
  .contact-list li {
    font-size: 15px; color: var(--text-white);
    line-height: 26px; white-space: nowrap;
  }
  .address {
    position: absolute; right: 36px; top: 216px;
    font-size: 15px; line-height: 22px; color: var(--text-white);
    text-align: right; white-space: nowrap;
  }

  /* Back */
  .brand-stack {
    position: absolute; inset: 0;
    display: flex; flex-direction: column; align-items: center; justify-content: center;
    gap: 18px;
  }
  .brand-name {
    font-weight: 700; font-size: 30px; letter-spacing: 3px;
    text-transform: uppercase; white-space: nowrap;
  }
  .brand-name--one { color: var(--accent-light); }
  .brand-name--two { color: var(--text-white); }
  .brand-name--three { color: var(--text-white); }
  .brand-rule {
    width: 300px; height: 2px;
    background: linear-gradient(90deg, transparent, #3f78c4 50%, transparent);
  }
</style>
</head>
<body>
  <section class="card card--front" aria-label="Business card front">
    <div class="parent-mark">
      <span class="parent-mark__dot"></span>
      <span class="parent-mark__name">MAPLE ROCK</span>
    </div>
    <div class="person">
      <p class="person__name">Daniel Reyes</p>
      <p class="person__title">Chief Operating Officer</p>
    </div>
    <div class="divider"></div>
    <ul class="contact-list">
      <li>555-014-2100</li>
      <li>hello@maplerockwash.com</li>
      <li>www.maplerockwash.com</li>
    </ul>
    <p class="address">Your address, city<br>state, ZIP 0000</p>
  </section>

  <section class="card card--back" aria-label="Business card back">
    <div class="brand-stack">
      <p class="brand-name brand-name--one">Sparkwave</p>
      <div class="brand-rule"></div>
      <p class="brand-name brand-name--two">Gloss Point</p>
      <div class="brand-rule"></div>
      <p class="brand-name brand-name--three">Harbor Mist</p>
    </div>
  </section>
</body>
</html>
```